Bref créative |
Velmora Web Design | ||
Web Site design | ||
Telecommunications | ||
www.velmora-example.com | ||
Velmora is a US based independent telecom services company providing expertise to mobile network operators and network equipment vendors around the world. Our core services are constructed around our unique competencies in post-processing drive test data, coupled with our years of experience working with various wireless technologies, including GSM/GPRS/EDGE, UMTS/HSPA+ and LTE. Our mission is to enable network operators to achieve the maximum possible return on their investment in drive test data collection. Our website will be used primarily by clients to see if they want to do business with us, and as such needs to clearly convey our main services while creating an overall impression of professionalism and competence. |
Likes: Clarity & simpliciity Ease of navigation Dislikes: Clutter Pictures of random business people Links to Facebook & Twitter |
Cutting-Edge Clean/Simple Professional Modern High Tech |
Blue - see logo | ||
Black/White | ||
Anything that fits with the logo | ||
below header | ||
The Home page will have 4 links: About Services Clients Contact The Services page will contain links to pages detailing the various services we offer, around 7 or so. The design should be simple and streamlined, and be easy to navigate without any unnecessary clutter. The design should complement the attached logo. |

```html
<!DOCTYPE html>
<html lang="en">
<head>
<meta charset="utf-8">
<title>Velmora Web Design</title>
<link rel="stylesheet" href="https://fonts.googleapis.com/css2?family=Arimo:ital,wght@0,400;0,700;1,400&family=Tinos:ital@1&display=swap">
<style>
:root{
  --navy:#0b1f4d;
  --navy-deep:#06163a;
  --blue:#1b4fa3;
  --sky:#6fa8ff;
  --grey:#5d5d5d;
  --grey-dark:#3a3a3a;
  --line:#d9d9d9;
  --white:#ffffff;
  --text:#222222;
  --gold:#f2b705;
}
*{box-sizing:border-box;margin:0;padding:0}
html,body{width:1200px;height:945px;overflow:hidden;background:var(--white);font-family:"Arimo",Arial,sans-serif}
.page{position:relative;width:1200px;height:945px}
.top-rule{position:absolute;left:0;top:0;width:100%;height:6px;background:var(--navy)}
.brand{position:absolute;left:140px;top:22px;width:300px}
.brand-row{display:flex;align-items:center;gap:10px;margin-top:60px}
.brand-mark{flex-shrink:0;width:30px;height:30px;background:var(--navy)}
.brand-name{font-size:40px;font-weight:700;color:var(--navy);letter-spacing:1px;line-height:1}
.brand-tag{font-size:12px;color:var(--navy);margin-top:6px}
.nav{position:absolute;left:498px;top:120px;display:flex;gap:3px}
.nav a{display:block;width:115px;height:46px;line-height:46px;text-align:center;color:var(--white);font-size:15px;text-decoration:none;background:linear-gradient(#7a7a7a,var(--grey-dark))}
.nav a.current{background:linear-gradient(var(--blue),var(--navy))}
.hero{position:absolute;left:0;top:166px;width:100%;height:383px;background:radial-gradient(ellipse at 65% 30%,#25437f 0%,var(--navy) 55%,var(--navy-deep) 100%)}
.mission{position:absolute;left:410px;top:80px;width:700px;text-align:center;font-family:"Tinos",Georgia,serif;font-style:italic;color:var(--white)}
.mission .lead{font-size:31px}
.mission .big{font-size:48px;color:var(--sky);margin:24px 0 20px}
.mission .tail{font-size:31px}
.services{position:absolute;left:120px;top:171px;display:grid;grid-template-columns:115px 115px;gap:4px;z-index:2}
.tile{height:116px;background:linear-gradient(#2c5fb5,#0f2f72);color:var(--white);font-size:11px;text-align:center;display:flex;flex-direction:column;align-items:center;padding-top:18px;gap:8px;text-transform:uppercase;border:1px solid #6e87b8}
.tile.alt{background:linear-gradient(#6b6b6b,#2e2e2e)}
.tile svg{width:48px;height:48px}
.clients-title{position:absolute;left:400px;top:592px;font-size:24px;color:var(--text)}
.clients-title span{color:var(--blue)}
.clients-rule{position:absolute;left:400px;top:632px;width:690px;height:1px;background:var(--line)}
.clients{position:absolute;left:400px;top:664px;display:flex;gap:9px}
.client{width:107px;height:94px;border:1px solid var(--line);background:linear-gradient(var(--white),#f2f2f2);display:flex;align-items:center;justify-content:center;font-size:16px;font-weight:700;color:var(--grey-dark)}
.footer{position:absolute;left:0;top:830px;width:100%;height:115px;background:linear-gradient(var(--navy),var(--navy-deep));border-top:4px solid var(--blue)}
.quick{position:absolute;top:12px;display:flex;flex-direction:column;align-items:center;gap:4px;color:var(--gold);font-size:15px}
.quick svg{width:56px;height:56px}
.contact{position:absolute;right:52px;top:34px;text-align:right;color:var(--white);font-size:13px;line-height:32px}
</style>
</head>
<body>
<div class="page">
  <div class="top-rule"></div>
  <header class="brand">
    <div class="brand-row"><div class="brand-mark"></div><div class="brand-name">VELMORA</div></div>
    <div class="brand-tag">Bringing your wireless data to life</div>
  </header>
  <nav class="nav">
    <a class="current" href="#">Home</a><a href="#">About Us</a><a href="#">Services</a><a href="#">Clients</a><a href="#">Contact Us</a>
  </nav>
  <section class="hero">
    <div class="mission">
      <p class="lead">Our Mission is to Enable Network Operators to Achieve</p>
      <p class="big">The Maximum Possible Return</p>
      <p class="tail">On their Investment in Drive Test Data Collection</p>
    </div>
  </section>
  <section class="services">
    <div class="tile"><svg viewBox="0 0 48 48"><circle cx="24" cy="24" r="21" fill="none" stroke="#fff" stroke-width="3"/><rect x="15" y="16" width="18" height="16" fill="#fff"/></svg>Customized<br>Reporting</div>
    <div class="tile alt"><svg viewBox="0 0 48 48"><circle cx="24" cy="24" r="21" fill="none" stroke="#fff" stroke-width="3"/><path d="M14 30l8-12 6 8 6-6" stroke="#fff" stroke-width="3" fill="none"/></svg>Configured VIR<br>Solutions</div>
    <div class="tile alt"><svg viewBox="0 0 48 48"><circle cx="24" cy="24" r="21" fill="none" stroke="#fff" stroke-width="3"/><rect x="21" y="14" width="6" height="20" fill="#fff"/></svg>Independent<br>Testing</div>
    <div class="tile"><svg viewBox="0 0 48 48"><circle cx="24" cy="24" r="21" fill="none" stroke="#fff" stroke-width="3"/><circle cx="24" cy="22" r="4" fill="#fff"/><path d="M16 16a11 11 0 0 0 0 14M32 16a11 11 0 0 1 0 14" stroke="#fff" stroke-width="2.5" fill="none"/><rect x="23" y="26" width="2" height="10" fill="#fff"/></svg>Benchmarking</div>
    <div class="tile"><svg viewBox="0 0 48 48"><circle cx="24" cy="24" r="21" fill="none" stroke="#fff" stroke-width="3"/><path d="M3 24h42M24 3v42" stroke="#fff" stroke-width="2"/><ellipse cx="24" cy="24" rx="9" ry="21" fill="none" stroke="#fff" stroke-width="2"/></svg>Training</div>
    <div class="tile alt"><svg viewBox="0 0 48 48"><circle cx="24" cy="24" r="21" fill="none" stroke="#fff" stroke-width="3"/><circle cx="24" cy="24" r="6" fill="none" stroke="#fff" stroke-width="3"/></svg>Parameter<br>Auditing/Planning</div>
    <div class="tile alt"><svg viewBox="0 0 48 48"><circle cx="24" cy="24" r="21" fill="none" stroke="#fff" stroke-width="3"/><rect x="14" y="18" width="20" height="14" fill="none" stroke="#fff" stroke-width="3"/></svg>Before/After<br>Analysis</div>
    <div class="tile"><svg viewBox="0 0 48 48"><circle cx="24" cy="24" r="21" fill="none" stroke="#fff" stroke-width="3"/><path d="M14 32V18h8l3 3h9v11z" fill="#fff"/></svg>On Site<br>Deployment</div>
  </section>
  <h2 class="clients-title">Our <span>Clients</span></h2>
  <div class="clients-rule"></div>
  <div class="clients">
    <div class="client">Norvant</div><div class="client">Calexo</div><div class="client">Brisca</div><div class="client">Teliqo</div><div class="client">Mobara</div><div class="client">Quellar</div>
  </div>
  <footer class="footer">
    <div class="quick" style="left:130px"><svg viewBox="0 0 56 56"><circle cx="28" cy="28" r="24" fill="none" stroke="#f2b705" stroke-width="8"/><circle cx="28" cy="28" r="10" fill="#0b1f4d"/></svg>Support</div>
    <div class="quick" style="left:236px"><svg viewBox="0 0 56 56"><path d="M12 4h24l10 10v38H12z" fill="#f5e6b0"/><path d="M18 22h22M18 30h22M18 38h22" stroke="#8a7a40" stroke-width="3"/></svg>Upload</div>
    <div class="quick" style="left:332px"><svg viewBox="0 0 56 56"><circle cx="28" cy="28" r="25" fill="#e8e8e8"/></svg>Wiki</div>
    <div class="contact">
      <p>Suite 48, 902 Harbor Rd, Westbrook Park WBK, 456 - T 8 5550 1842</p>
      <p>Copyright © 2012 <strong>Velmora</strong>. All Rights Reserved</p>
    </div>
  </footer>
</div>
</body>
</html>
```